Fitness Coach Needs Book Cover Created

I would like a book cover created for my upcoming project titled,
Steady Stride After Forty: 9 Quiet Rituals for a Brighter Routine

Target Market(s)

Men & Women 30-40 years old

Industry/Entity Type

Fitness

Font styles to use
Serif

Requirements
Must have
• 3 color cover. I have attached my name to be used at bottom of cover and uploaded a couple sample covers as well.
Should not have
• stock imaging.

```html
<!DOCTYPE html>
<html lang="en">
<head>
<meta charset="utf-8">
<title>Steady Stride After Forty — Book Cover</title>
<link href="https://fonts.googleapis.com/css2?family=Montserrat:wght@300;400;700;800&display=swap" rel="stylesheet">
<style>
  :root {
    --blue-deep: #1a64a6;
    --blue-mid: #2f93cf;
    --blue-light: #63c1e8;
    --ink: #0c1c30;
  }
  html, body {
    margin: 0;
    padding: 0;
    width: 800px;
    height: 1200px;
    overflow: hidden;
    background: var(--blue-deep);
  }
  .cover {
    position: relative;
    width: 800px;
    height: 1200px;
    overflow: hidden;
    font-family: "Montserrat", sans-serif;
    color: var(--ink);
    background:
      radial-gradient(ellipse 75% 55% at 50% 48%, rgba(120, 210, 245, 0.55) 0%, rgba(120, 210, 245, 0) 70%),
      linear-gradient(180deg, var(--blue-deep) 0%, var(--blue-mid) 22%, var(--blue-light) 52%, var(--blue-mid) 75%, var(--blue-deep) 100%);
  }
  .cover::after {
    content: "";
    position: absolute;
    inset: 0;
    background: radial-gradient(ellipse 95% 85% at 50% 50%, rgba(0,0,0,0) 60%, rgba(10, 40, 90, 0.35) 100%);
    pointer-events: none;
  }
  .title-block {
    position: absolute;
    top: 238px;
    left: 0;
    width: 100%;
    text-align: center;
  }
  .title-kicker {
    margin: 0;
    font-weight: 300;
    font-size: 40px;
    letter-spacing: 1px;
    line-height: 1;
  }
  .title-main {
    margin: 26px 0 0;
    font-weight: 700;
    font-size: 104px;
    letter-spacing: 1px;
    line-height: 1;
  }
  .subtitle {
    margin: 58px 0 0;
    font-weight: 400;
    font-size: 31px;
    letter-spacing: 3px;
    line-height: 1.42;
  }
  .author {
    position: absolute;
    bottom: 124px;
    left: 0;
    width: 100%;
    margin: 0;
    text-align: center;
    font-weight: 800;
    font-size: 50px;
    letter-spacing: 2px;
    color: var(--ink);
    z-index: 1;
  }
</style>
</head>
<body>
  <main class="cover">
    <header class="title-block">
      <p class="title-kicker">STEADY STRIDE</p>
      <h1 class="title-main">AFTER FORTY:</h1>
      <p class="subtitle">9 QUIET RITUALS FOR A<br>BRIGHTER ROUTINE</p>
    </header>
    <p class="author">ROSS ADLER</p>
  </main>
</body>
</html>
```